Design für Sprüche Darstellung
Zielgruppe
www.zitronenhafen-blatt.org ist eine der größten Sprüche Seiten im Netz. Mit monatlich ca. 800.000 Aufrufen.
Für unsere Plauderwand Seite (https://www.plauderwand.net/ZitronenhafenBlatt/) suchen wir ein neues Spruch Design für unsere Posts.
Wie Sie auf der Plauderwand Seite sehen, erstellen wir viele Spruchbilder bereits mit passenden Hintergründen.
Ihr Aufgabe ist es ein Design zu entwerfen, dass wir für die übrigen Sprüche verwenden möchten. Also für die Sprüche, die kein extra Spruchbild mit Hintergrund bekommen.
Diese sollen trotzdem auch durch kreative Schriftarten und Gestaltung Aufmerksamkeit generieren.
Aufgabenstellung
Erstellung einer quadratischen Photoshop Vorlage die für eine Vielzahl an Sprüchen und Zitaten verwendet werden kann.
Passender Hintergrund + Schriftart.
Weiterhin soll unser Logo sowie die Webadresse mit darauf platziert werden.

```html
<!DOCTYPE html>
<html lang="de">
<head>
<meta charset="utf-8">
<title>Zitronenhafen Blatt – Spruch</title>
<link rel="stylesheet" href="https://fonts.googleapis.com/css2?family=Bebas+Neue&family=Roboto:wght@400&display=swap">
<style>
  :root {
    --frame: #000000;
    --sky-light: #f4f4f4;
    --sky-mid: #e6e6e6;
    --sky-soft: #dcdcdc;
    --ink: #111111;
    --url-ink: #222222;
  }
  html, body {
    margin: 0;
    padding: 0;
    width: 1200px;
    height: 1200px;
    overflow: hidden;
    background: var(--frame);
  }
  .post {
    position: relative;
    width: 1200px;
    height: 1200px;
    box-sizing: border-box;
    border: 42px solid var(--frame);
    overflow: hidden;
  }
  .post__backdrop {
    position: absolute;
    inset: 0;
    background:
      radial-gradient(ellipse 60% 30% at 30% 18%, var(--sky-light) 0%, transparent 70%),
      radial-gradient(ellipse 55% 25% at 75% 85%, var(--sky-light) 0%, transparent 70%),
      radial-gradient(ellipse 80% 60% at 50% 50%, var(--sky-light) 0%, var(--sky-mid) 75%, var(--sky-soft) 100%);
  }
  .quote {
    position: absolute;
    left: 241px;
    top: 332px;
    width: 720px;
    margin: 0;
    font-family: "Bebas Neue", "Arial Narrow", sans-serif;
    font-weight: 400;
    font-size: 70px;
    line-height: 72px;
    letter-spacing: 1px;
    color: var(--ink);
    text-transform: uppercase;
  }
  .brand {
    position: absolute;
    left: 0;
    right: 0;
    top: 948px;
    display: flex;
    justify-content: center;
    align-items: center;
    gap: 18px;
  }
  .brand__dot {
    width: 44px;
    height: 44px;
    border-radius: 50%;
    background: var(--ink);
  }
  .brand__name {
    font-family: "Bebas Neue", "Arial Narrow", sans-serif;
    font-size: 64px;
    line-height: 1;
    color: var(--ink);
    letter-spacing: 1px;
  }
  .site-url {
    position: absolute;
    left: 0;
    right: 0;
    top: 1080px;
    text-align: center;
    font-family: "Roboto", Arial, sans-serif;
    font-size: 32px;
    color: var(--url-ink);
  }
</style>
</head>
<body>
  <main class="post">
    <div class="post__backdrop" role="img" aria-label="Heller, grauweißer Wolkenhimmel als Hintergrund"></div>
    <p class="quote">Wenn dir etwas wichtig ist,<br>wirst du einen Weg finden.<br>Wenn dir etwas nicht wichtig<br>ist, wirst du eine Ausrede<br>finden.</p>
    <div class="brand">
      <span class="brand__dot"></span>
      <span class="brand__name">Zitronenhafen Blatt</span>
    </div>
    <div class="site-url">www.zitronenhafen-blatt.org</div>
  </main>
</body>
</html>
```